K&T Fixit and Rebuild general contracting business card design

I already have a logo that I want to use and I need a card that uses that logo and color scheme on the front with the address phone numbers and email and on the back a place for technicians to write in their name and phone number when they hand it out. It will need the License number of License #KTFXTRB318QN.
It should say General Contractor under the company name. The address is
4417 NE 3rd Ave, Ste D246
Vancouver, WA 98612
www.kandtfixitandrebuild.example
office@kandtfixitandrebuild.example
360-555-0182 is the telephone number
360-555-0149 is the fax number

Target Market(s)

Homeowners needing remodel work or repairs in their home.

Industry/Entity Type

Construction

Contact Information for Business Card

Business name, address, phone number, license number, fax number, email, and website on the front and a place to fill in technician's name and number

Font styles to use
Serif

Requirements
Must have
• Business name, address, phone number, license number, fax number, email, and website on the front and a place to fill in technician's name and number
Nice to have
• I uploaded an example of a front that is good.
Should not have
• Froo froo or extra embellishments.

```html
<!DOCTYPE html>
<html lang="en">
<head>
<meta charset="utf-8">
<title>K&amp;T Fixit and Rebuild – Business Card</title>
<link href="https://fonts.googleapis.com/css2?family=Source+Serif+4:opsz,wght@8..60,400;8..60,600;8..60,700;8..60,900&display=swap" rel="stylesheet">
<style>
  :root {
    --backdrop: #8f8f8f;
    --card-white: #ffffff;
    --ink: #1f1f1f;
    --brand-red: #a21d22;
    --brand-brown: #a5603a;
    --brand-copper: #b86a3e;
    --wood: #e5b899;
    --wood-deep: #c98f6c;
    --wood-line: #a9714f;
    --white: #ffffff;
  }
  * { margin: 0; padding: 0; box-sizing: border-box; }
  html, body { width: 1200px; height: 1200px; overflow: hidden; }
  body {
    background: var(--backdrop);
    font-family: "Source Serif 4", serif;
    display: flex;
    flex-direction: column;
    align-items: center;
    justify-content: center;
    gap: 60px;
  }
  .card {
    width: 840px;
    height: 478px;
    position: relative;
    overflow: hidden;
  }
  /* Front */
  .card-front { background: var(--card-white); color: var(--ink); }
  .brand {
    position: absolute;
    left: 440px;
    top: 80px;
    width: 360px;
    text-align: center;
  }
  .brand-name {
    font-weight: 700;
    font-size: 48px;
    line-height: 1.08;
    color: var(--brand-brown);
  }
  .brand-tagline {
    margin-top: 20px;
    font-size: 21px;
    letter-spacing: 0.5px;
    color: var(--brand-copper);
  }
  .address {
    position: absolute;
    left: 57px;
    top: 192px;
    font-size: 22px;
    line-height: 1.4;
  }
  .contacts {
    position: absolute;
    left: 57px;
    top: 276px;
    list-style: none;
    font-size: 22px;
    line-height: 1.45;
  }
  .contacts li { display: flex; align-items: center; gap: 10px; }
  .contacts svg { width: 26px; height: 22px; flex: none; }
  .footer-band {
    position: absolute;
    left: 0; right: 0; bottom: 0;
    height: 82px;
    background: var(--brand-red);
    color: var(--white);
    display: flex;
    align-items: center;
    justify-content: space-between;
    padding: 0 57px;
  }
  .website { font-weight: 700; font-size: 27px; }
  .license { font-size: 19px; }
  /* Back */
  .card-back { background: var(--wood); }
  .wood-surface {
    position: absolute; inset: 0;
    background: linear-gradient(100deg, #e9bfa1 0%, var(--wood) 45%, #e2b493 100%);
  }
  .back-name {
    position: absolute;
    left: 0; right: 0; top: 56px;
    text-align: center;
    font-weight: 700;
    font-size: 62px;
    line-height: 1.08;
    color: var(--wood-deep);
  }
  .write-in {
    position: absolute;
    left: 90px; right: 90px; top: 268px;
    list-style: none;
    display: flex;
    flex-direction: column;
    gap: 44px;
  }
  .write-in li {
    display: flex;
    align-items: flex-end;
    gap: 16px;
    font-size: 22px;
    font-weight: 600;
    color: var(--wood-line);
  }
  .write-in .label { width: 130px; flex: none; }
  .write-in .blank {
    flex: 1;
    border-bottom: 2px solid var(--wood-line);
    height: 26px;
  }
</style>
</head>
<body>

  <section class="card card-front" aria-label="Business card front">
    <div class="brand">
      <div class="brand-name">K&amp;T Fixit<br>and Rebuild</div>
      <div class="brand-tagline">GENERAL CONTRACTOR</div>
    </div>

    <p class="address">4417 NE 3rd Ave, Ste D246<br>Vancouver, WA 98612</p>

    <ul class="contacts">
      <li>
        <svg viewBox="0 0 26 22" aria-hidden="true"><path d="M6 3 C3 5 3 9 7 14 C11 19 15 20 18 18 L15 14 L12 15 C10 13 9 11 8.5 9 L11 7 Z" fill="none" stroke="var(--brand-red)" stroke-width="1.6" stroke-linejoin="round"/></svg>
        360-555-0182
      </li>
      <li>
        <svg viewBox="0 0 26 22" aria-hidden="true"><g fill="none" stroke="var(--brand-red)" stroke-width="1.5"><rect x="3" y="8" width="20" height="13"/><rect x="8" y="2" width="10" height="6"/><rect x="5" y="11" width="4" height="8"/><path d="M12 12h2M16 12h2M12 15h2M16 15h2M12 18h2M16 18h2"/></g></svg>
        360-555-0149
      </li>
      <li>
        <svg viewBox="0 0 26 22" aria-hidden="true"><g fill="none" stroke="var(--brand-red)" stroke-width="1.6"><rect x="2" y="4" width="22" height="15"/><path d="M2 4 L13 13 L24 4"/></g></svg>
        office@kandtfixitandrebuild.example
      </li>
    </ul>

    <div class="footer-band">
      <span class="website">kandtfixitandrebuild.example</span>
      <span class="license">License #KTFXTRB318QN</span>
    </div>
  </section>

  <section class="card card-back" aria-label="Business card back">
    <div class="wood-surface" role="img" aria-label="Light wood grain surface"></div>
    <div class="back-name">K&amp;T Fixit<br>and Rebuild</div>
    <ul class="write-in">
      <li><span class="label">Technician</span><span class="blank"></span></li>
      <li><span class="label">Phone</span><span class="blank"></span></li>
    </ul>
  </section>

</body>
</html>
```